Business Card Design Project

I am opening my own real estate company.

Tarrow & Co. Real Estate Inc.

See attachments for ideas and colors…..
Updates

Project Deadline Extended
Reason: I paid for 5 separate items (graphic design, logo, stationery, brochure & website) all at one time. I thought they all launched at the same time but they did not. That is the reason I have to extend the date.

Target Market(s)

High end real estate properties.

Industry/Entity Type

Real Estate

Font styles to use
Serif
Decorative
Script

Requirements
Must have
• High end design. I want to appeal to very expensive properties.

```html
<!DOCTYPE html>
<html lang="en">
<head>
<meta charset="utf-8">
<title>Tarrow &amp; Co. Real Estate Inc. – Business Card</title>
<link rel="stylesheet" href="https://fonts.googleapis.com/css2?family=Marcellus&family=Marcellus+SC&display=swap">
<style>
  :root {
    --backdrop: #2a2928;
    --card-brown: #3d2c18;
    --card-brown-deep: #33240f;
    --band-tan: #7b603c;
    --band-tan-light: #8a6d46;
    --ornament-tone: #d9d2c6;
    --ink-light: #f4efe6;
    --stripe-white: #f7f5f1;
  }

  * { margin: 0; padding: 0; box-sizing: border-box; }

  html, body {
    width: 1200px;
    height: 798px;
    overflow: hidden;
    background: var(--backdrop);
  }

  .canvas {
    width: 1200px;
    height: 798px;
    display: flex;
    align-items: center;
    justify-content: center;
  }

  .business-card {
    position: relative;
    width: 1000px;
    height: 572px;
    background: var(--card-brown);
    overflow: hidden;
    font-family: "Marcellus SC", "Times New Roman", serif;
    color: var(--ink-light);
  }

  .swirl-field {
    position: absolute;
    inset: 0 0 180px 0;
    background:
      radial-gradient(ellipse 260px 200px at 58% 58%, rgba(107, 82, 50, 0.55), transparent 70%),
      radial-gradient(ellipse 220px 160px at 18% 70%, rgba(107, 82, 50, 0.35), transparent 70%),
      linear-gradient(180deg, var(--card-brown) 0%, var(--card-brown-deep) 100%);
  }

  .ornament {
    position: absolute;
    height: 70px;
    background: var(--ornament-tone);
    opacity: 0.22;
    border-radius: 36px;
  }
  .ornament--left  { left: 60px;  top: 40px;  width: 170px; }
  .ornament--right { right: 50px; top: 40px;  width: 170px; }

  .brand {
    position: absolute;
    top: 150px;
    left: 0;
    width: 100%;
    text-align: center;
    font-family: "Marcellus", "Times New Roman", serif;
    font-weight: 400;
    font-size: 38px;
    letter-spacing: 1px;
    line-height: 1;
  }

  .holder {
    position: absolute;
    top: 258px;
    left: 0;
    width: 100%;
    text-align: center;
    line-height: 1;
  }
  .holder-name {
    display: block;
    font-size: 66px;
    letter-spacing: 2px;
  }
  .holder-title {
    display: block;
    margin-top: 8px;
    font-size: 30px;
    letter-spacing: 1px;
  }

  .contact-band {
    position: absolute;
    left: 0;
    right: 0;
    bottom: 0;
    height: 184px;
  }
  .stripe {
    position: absolute;
    left: 0;
    right: 0;
    height: 10px;
    background: var(--stripe-white);
  }
  .stripe--top { top: 0; }
  .stripe--bottom { bottom: 26px; }

  .contact-fill {
    position: absolute;
    left: 0;
    right: 0;
    top: 10px;
    bottom: 36px;
    background: linear-gradient(180deg, var(--band-tan-light), var(--band-tan));
  }
  .contact-foot {
    position: absolute;
    left: 0;
    right: 0;
    bottom: 0;
    height: 26px;
    background: var(--band-tan);
  }

  .contact-web,
  .contact-phone {
    position: absolute;
    font-size: 28px;
    letter-spacing: 1px;
    line-height: 1;
    color: var(--ink-light);
  }
  .contact-web   { left: 48px;  top: 40px; }
  .contact-phone { right: 60px; top: 96px; }
</style>
</head>
<body>
  <main class="canvas">
    <article class="business-card">
      <div class="swirl-field" role="img" aria-label="Soft brown flowing swirl pattern across the card background"></div>

      <div class="ornament ornament--left" role="img" aria-label="Decorative white scroll flourish"></div>
      <div class="ornament ornament--right" role="img" aria-label="Decorative white scroll flourish"></div>

      <h1 class="brand">Tarrow &amp; Co. Real Estate Inc.</h1>

      <p class="holder">
        <span class="holder-name">Your Name</span>
        <span class="holder-title">Job Title</span>
      </p>

      <footer class="contact-band">
        <div class="stripe stripe--top"></div>
        <div class="contact-fill"></div>
        <div class="stripe stripe--bottom"></div>
        <div class="contact-foot"></div>
        <span class="contact-web">www.tarrowhomes.com</span>
        <span class="contact-phone">Tel: (555) 204-7319</span>
      </footer>
    </article>
  </main>
</body>
</html>
```